Baby Boutique Needs a Business Card Design

We need a modern double sided business card design using the attached logo for T' Tot Nook.

T' Tot Nook is a baby boutique which sells only handmade clothing and accessories for both boys and girls. Our store will live exclusively online.

We would like to only use the colors that have been used in the logo.

Target Market(s)

Potential wholesale clients, Small business owners

Industry/Entity Type

Retail

Contact Information for Business Card

Name Benedict R. Halvorsen (Owner)
Email sales@ttotnook.example
Main Phone 555-203-7164
Cell phone 555-203-7590
Website www.TTotNook.example

Font styles to use
Sans Serif

Colors

Designer to choose colors to be used in the design.

Requirements
Must have
• -Would like to have icons that indentify the contact information.
• -Include our website
• -Include our tagline in a small area near the bottom. "Handmade Baby Creations"
• -Would like to include Facepage and Snapgram Icons
• -
Nice to have
• Would like to have a simple back side with the logo.
• Something along the lines of the meridale funding card attached.

```html
<!DOCTYPE html>
<html lang="en">
<head>
<meta charset="utf-8">
<title>T' Tot Nook — Business Card</title>
<link href="https://fonts.googleapis.com/css2?family=Work+Sans:wght@400;500;600&display=swap" rel="stylesheet">
<style>
  :root {
    --backdrop: #3a302c;
    --card: #1c1c1d;
    --mint: #6fd3c0;
    --coral: #ea5f5f;
    --white: #f2f2f2;
  }
  * { margin: 0; padding: 0; box-sizing: border-box; }
  html, body { width: 1200px; height: 715px; overflow: hidden; }
  body {
    background: var(--backdrop);
    font-family: "Work Sans", sans-serif;
    position: relative;
  }
  .card {
    position: absolute;
    width: 540px;
    height: 309px;
    background: var(--card);
    overflow: hidden;
    box-shadow: 0 10px 30px rgba(0,0,0,.45);
  }
  .card--back { left: 40px; top: 203px; }
  .card--front { left: 620px; top: 203px; }

  .brand {
    color: var(--mint);
    font-weight: 600;
    line-height: 1;
    white-space: nowrap;
  }
  .card--back .brand {
    position: absolute;
    left: 0; right: 0; top: 128px;
    text-align: center;
    font-size: 44px;
  }
  .card--front .brand {
    position: absolute;
    left: 40px; top: 36px;
    font-size: 30px;
  }

  .divider {
    position: absolute;
    left: 40px; right: 40px; top: 150px;
    height: 1px;
    background: var(--coral);
  }

  .contact {
    position: absolute;
    left: 40px; top: 164px;
    list-style: none;
    color: var(--white);
    font-size: 12.5px;
    line-height: 17px;
  }
  .contact li { display: flex; align-items: center; gap: 7px; }
  .contact svg { width: 9px; height: 9px; flex: none; }

  .person {
    position: absolute;
    right: 40px; top: 112px;
    text-align: right;
  }
  .person__name { color: var(--coral); font-size: 20px; font-weight: 500; }
  .person__role { color: var(--white); font-size: 12.5px; margin-top: 1px; }

  .social {
    position: absolute;
    right: 40px; top: 238px;
    display: flex; gap: 12px;
    color: var(--coral);
    font-size: 11px;
    font-weight: 500;
  }

  .band-mint {
    position: absolute;
    left: 0; bottom: 0;
    width: 300px; height: 8px;
    background: var(--mint);
  }
  .band-coral {
    position: absolute;
    right: 0; bottom: 0;
    width: 260px; height: 30px;
    background: var(--coral);
    clip-path: polygon(28px 0, 100% 0, 100% 100%, 0 100%);
    color: var(--white);
    font-size: 12.5px;
    display: flex; align-items: center; justify-content: flex-end;
    padding-right: 40px;
  }
</style>
</head>
<body>
  <section class="card card--back" aria-label="Card back">
    <div class="brand">T' Tot Nook</div>
  </section>

  <section class="card card--front" aria-label="Card front">
    <div class="brand">T' Tot Nook</div>
    <div class="divider"></div>

    <ul class="contact">
      <li>
        <svg viewBox="0 0 10 10"><path d="M2 1l2 2-1 1.2c.6 1.3 1.5 2.2 2.8 2.8L7 6l2 2-1.3 1.3C4.5 9 1 5.5.7 2.3z" fill="var(--coral)"/></svg>
        555-203-7164
      </li>
      <li>
        <svg viewBox="0 0 10 10"><rect x="2.5" y=".5" width="5" height="9" rx="1" fill="none" stroke="var(--coral)"/><circle cx="5" cy="8" r=".6" fill="var(--coral)"/></svg>
        555-203-7590
      </li>
      <li>
        <svg viewBox="0 0 10 10"><rect x=".5" y="2" width="9" height="6" fill="none" stroke="var(--coral)"/><path d="M.5 2L5 5.5 9.5 2" fill="none" stroke="var(--coral)"/></svg>
        sales@ttotnook.example
      </li>
      <li>
        <svg viewBox="0 0 10 10"><circle cx="5" cy="5" r="4.5" fill="none" stroke="var(--coral)"/><path d="M.5 5h9M5 .5c-2 2.5-2 6.5 0 9M5 .5c2 2.5 2 6.5 0 9" fill="none" stroke="var(--coral)" stroke-width=".7"/></svg>
        www.TTotNook.example
      </li>
    </ul>

    <div class="person">
      <div class="person__name">Benedict R. Halvorsen</div>
      <div class="person__role">Owner</div>
    </div>

    <div class="social">
      <span>Facepage</span>
      <span>Snapgram</span>
    </div>

    <div class="band-mint"></div>
    <div class="band-coral">Handmade Baby Creations</div>
  </section>
</body>
</html>
```